Redesign/Facelift for Affiliate Shopping Fashion Site

We are velunix, Fashion web site from Berlin, Germany,
looking to redesign/facelift our affiliate shopping site,
http://shop.velunix.de/bekleidung,84rtpa21xuwdnc90,ec_sale,sa
(Main page view)
http://shop.velunix.de/lorn-gale-seidentunika-pemby,3kdh5w1rcyt8ae6v,i
(Single article view)

Altogether we want to make it more coherent, key words being
MINIMAL and STYLISH.

NOTE:
You don´t need to completely design both pages, it would be sufficient to propose a direction you would take. However, we should be able to envision the complete solution.

The solution should be similar to another comparable affiliate site,
http://www.kaufzirkel.de/browse/damen-kleidung

- - General Brief:
The design should have an overall aesthetic coherence,
especially when it comes to sizes of elements
and the bars like in the side bar left, or "Zum Shop".
The solution should be done for the main page and the single article page.

- - Here are the elements in particular, and how they should be designed:
- Main Page HEADER BAR (and single article page) elements:
header bar extends across the entire width of the screen
our logo
"Shopping" text next to the logo
search form
categories "Bekleidung, Accessoires, Schmuck" etc.
Plimbora and zappel buttons

- Main page SIDEBAR (left):
elements as can be seen
menu "Preis" is replaced by a price "slider" to more accurately determine
a shopping price range

- Main page PRODUCTS:
elements as can be seen
the "% discount" symbol and "Zum Shop" elements especially
should be looked at

- Main page (and single article page) FOOTER:
should extend across the entire width of the screen

- Single article page
(http://shop.velunix.de/lorn-gale-seidentunika-pemby,3kdh5w1rcyt8ae6v,i)
header and footer as discussed for the Main page
bars (below the article) "Ähnliche Produkte zu….", "Weitere Produkte…" should be replaced by
"lighter" solution

Thank you,
feel free to ask question if something is not clear.
Telmo

```html
<!DOCTYPE html>
<html lang="de">
<head>
<meta charset="utf-8">
<title>velunix – Bekleidung</title>
<link href="https://fonts.googleapis.com/css2?family=Oswald:wght@700&family=Open+Sans:wght@400;600&display=swap" rel="stylesheet">
<style>
:root{
  --teal:#1a9ec2;
  --teal-light:#14b3d8;
  --teal-dark:#0f8cae;
  --black:#111;
  --orange:#f26a1b;
  --text:#333;
  --muted:#666;
  --white:#fff;
  --line:#e2e2e2;
}
*{box-sizing:border-box;margin:0;padding:0}
html,body{width:1200px;height:1010px;overflow:hidden;background:var(--white);font-family:"Open Sans",Arial,sans-serif;color:var(--text)}
.page{position:relative;width:1200px;height:1010px}

.topbar{position:absolute;left:0;top:0;width:1200px;height:100px;background:var(--teal)}
.brand{position:absolute;left:130px;top:30px;font-family:"Oswald",Arial,sans-serif;font-weight:700;font-size:29px;color:var(--white);letter-spacing:.5px}
.main-nav{position:absolute;right:128px;top:30px;display:flex;height:36px;border-left:1px solid rgba(255,255,255,.25)}
.main-nav a{color:var(--white);text-decoration:none;font-size:18px;padding:6px 23px 0;border-right:1px solid rgba(255,255,255,.25)}

.hero{position:absolute;left:0;top:100px;width:1200px;height:400px;display:flex}
.hero .look{height:100%}
.look-1{width:237px;background:linear-gradient(180deg,#c9bfa6,#d9cf8a 40%,#c8b86a)}
.look-2{width:277px;background:linear-gradient(180deg,#bdb3a8,#e6e2dc 40%,#c9c2b9)}
.look-3{width:237px;background:linear-gradient(180deg,#b8a28e,#2d7f99 40%,#256f88)}
.look-4{width:223px;background:linear-gradient(180deg,#a89a90,#8a8c9c 40%,#6f7180)}
.look-5{width:226px;background:linear-gradient(180deg,#a38c7a,#4a1e22 40%,#2e1214)}
.search-panel{position:absolute;left:248px;top:250px;width:706px;height:88px;background:rgba(40,40,40,.72)}
.search-input{position:absolute;left:15px;top:18px;width:562px;height:53px;background:var(--white);font-size:12px;color:#999;padding:24px 10px 0}
.search-btn{position:absolute;left:593px;top:18px;width:96px;height:53px;background:var(--teal);color:var(--white);font-size:18px;text-align:center;line-height:53px}

.cat-bar{position:absolute;left:0;top:500px;width:1200px;height:50px;background:var(--black)}
.cat-bar ul{list-style:none;display:flex;gap:20px;position:absolute;left:131px;top:16px}
.cat-bar li{color:var(--white);font-size:13px}

.toolbar{position:absolute;left:689px;top:591px;display:flex;align-items:center;font-size:11px;color:var(--text)}
.check{width:10px;height:10px;border:1px solid #888;margin-right:4px;display:flex;align-items:center;justify-content:center}
.sort-label{margin-left:20px;margin-right:3px}
.select{width:117px;height:16px;border:1px solid #aaa;font-size:11px;padding-left:4px;position:relative;line-height:14px}
.select::after{content:"";position:absolute;right:0;top:0;width:15px;height:14px;border-left:1px solid #aaa;background:#eee}
.view-icons{margin-left:8px;display:flex;gap:5px}

.sidebar{position:absolute;left:129px;top:615px;width:174px}
.side-head{height:36px;background:var(--teal-light);color:var(--white);font-size:15px;padding:8px 15px}
.radio-list{list-style:none;padding:8px 0 12px 14px;font-size:12px}
.radio-list li{display:flex;align-items:center;height:18px}
.radio-list li::before{content:"";width:7px;height:7px;border:1px solid #888;border-radius:50%;margin-right:8px}
.cat-list{position:relative;height:230px;margin-bottom:21px}
.cat-list ul{list-style:none;padding:6px 0 0 16px;font-size:12px;line-height:18px}
.scroll{position:absolute;right:3px;top:5px;width:15px;height:222px;background:#f1f1f1;border:1px solid #ddd}
.scroll .thumb{position:absolute;left:1px;top:18px;width:11px;height:88px;background:#ddd;border:1px solid #bbb}

.grid{position:absolute;left:320px;top:615px;display:grid;grid-template-columns:repeat(4,181px);column-gap:8.5px;row-gap:8px}
.card{width:181px;height:328px;border:1px solid var(--line)}
.card-title{height:35px;background:var(--black);color:var(--white);font-size:12px;padding:9px 10px}
.card-media{position:relative;height:200px;display:flex;justify-content:center;align-items:center}
.dress{width:70px;height:176px;border-radius:30px 30px 6px 6px;background:linear-gradient(180deg,#cfd8dc,#b9c7d6 40%,#c78fa0 70%,#a35a6a)}
.badge{position:absolute;right:6px;top:71px;width:58px;height:31px;background:var(--orange);color:var(--white);font-size:17px;text-align:center;line-height:31px}
.card-price{height:60px;background:var(--teal);color:var(--white);padding:12px 8px 0;position:relative}
.price{font-weight:600;font-size:16px}
.old{font-size:11px;text-decoration:line-through;opacity:.85}
.ship{position:absolute;right:12px;top:15px;font-size:12px}
.shop-btn{height:33px;background:var(--teal-light);color:var(--white);font-size:15px;display:flex;align-items:center;justify-content:center;gap:8px}
</style>
</head>
<body>
<div class="page">
  <header class="topbar">
    <div class="brand">VELUNIX</div>
    <nav class="main-nav"><a>News</a><a>Velunix.tv</a><a>Selection</a><a>Fashion Art</a></nav>
  </header>

  <section class="hero">
    <div class="look look-1" role="img" aria-label="Laufstegfoto: Model in goldfarbener bestickter Tunika"></div>
    <div class="look look-2" role="img" aria-label="Laufstegfoto: Model in weißem Tüllkleid"></div>
    <div class="look look-3" role="img" aria-label="Laufstegfoto: Model in türkisfarbenem besticktem Kleid"></div>
    <div class="look look-4" role="img" aria-label="Laufstegfoto: Model in grauem drapiertem Spitzenkleid"></div>
    <div class="look look-5" role="img" aria-label="Laufstegfoto: Model in dunkelrotem Kleid mit Goldstickerei"></div>
    <div class="search-panel">
      <div class="search-input">Wonatch Suchst Du?</div>
      <div class="search-btn">Suchen</div>
    </div>
  </section>

  <nav class="cat-bar">
    <ul><li>Bekleidung</li><li>Accessoires</li><li>Schmuck</li><li>Schuhe</li><li>Taschen</li><li>Uhren</li><li>Beauty</li><li>Wohnen</li><li>Haushalt</li><li>Drogerie</li><li>Sport und Freizeit</li><li>Spielzeug</li></ul>
  </nav>

  <div class="toolbar">
    <span class="check"><svg width="8" height="8" viewBox="0 0 8 8"><path d="M1 4l2 2 4-5" stroke="#333" stroke-width="1.4" fill="none"/></svg></span>
    Nur reduzierte Artikel
    <span class="sort-label">Sortieren nach:</span>
    <span class="select">Beliebteste</span>
    <span class="view-icons">
      <svg width="11" height="11" viewBox="0 0 11 11" fill="#e0458a"><rect width="3" height="3"/><rect x="4" width="3" height="3"/><rect x="8" width="3" height="3"/><rect y="4" width="3" height="3"/><rect x="4" y="4" width="3" height="3"/><rect x="8" y="4" width="3" height="3"/><rect y="8" width="3" height="3"/><rect x="4" y="8" width="3" height="3"/><rect x="8" y="8" width="3" height="3"/></svg>
      <svg width="11" height="11" viewBox="0 0 11 11" fill="#e0458a"><rect width="11" height="2"/><rect y="3" width="11" height="2"/><rect y="6" width="11" height="2"/><rect y="9" width="11" height="2"/></svg>
    </span>
  </div>

  <aside class="sidebar">
    <div class="side-head">Geschlecht</div>
    <ul class="radio-list"><li>männlich</li><li>weiblich</li></ul>
    <div class="side-head">Kategorien</div>
    <div class="cat-list">
      <ul><li>Anzüge (136)</li><li>Bademode (4863)</li><li>Blazer (916)</li><li>Blusen (2799)</li><li>Wäsche (3936)</li><li>Hemden (12298)</li><li>Homewear (99)</li><li>Hosen (53299)</li><li>Jacken (27687)</li><li>Jeans (22264)</li><li>Kleider (45055)</li><li>Mäntel (542</li></ul>
      <div class="scroll"><div class="thumb"></div></div>
    </div>
    <div class="side-head">Marken</div>
  </aside>

  <main class="grid">
    <article class="card"><div class="card-title">Druckkleid, bunt</div><div class="card-media"><div class="dress" role="img" aria-label="Produktfoto: bunt bedrucktes Kleid"></div><span class="badge">- 24%</span></div><div class="card-price"><div class="price">37.99 €</div><div class="old">49.90 €</div><span class="ship">Versand: +5,95</span></div><div class="shop-btn"><svg width="20" height="16" viewBox="0 0 20 16" fill="none" stroke="#fff" stroke-width="1.5"><path d="M1 1h3l2 9h10l2-6H5"/><circle cx="8" cy="13.5" r="1.3"/><circle cx="15" cy="13.5" r="1.3"/></svg>Zum Shop</div></article>
    <article class="card"><div class="card-title">Druckkleid, bunt</div><div class="card-media"><div class="dress" role="img" aria-label="Produktfoto: bunt bedrucktes Kleid"></div><span class="badge">- 24%</span></div><div class="card-price"><div class="price">37.99 €</div><div class="old">49.90 €</div><span class="ship">Versand: +5,95</span></div><div class="shop-btn"><svg width="20" height="16" viewBox="0 0 20 16" fill="none" stroke="#fff" stroke-width="1.5"><path d="M1 1h3l2 9h10l2-6H5"/><circle cx="8" cy="13.5" r="1.3"/><circle cx="15" cy="13.5" r="1.3"/></svg>Zum Shop</div></article>
    <article class="card"><div class="card-title">Druckkleid, bunt</div><div class="card-media"><div class="dress" role="img" aria-label="Produktfoto: bunt bedrucktes Kleid"></div><span class="badge">- 24%</span></div><div class="card-price"><div class="price">37.99 €</div><div class="old">49.90 €</div><span class="ship">Versand: +5,95</span></div><div class="shop-btn"><svg width="20" height="16" viewBox="0 0 20 16" fill="none" stroke="#fff" stroke-width="1.5"><path d="M1 1h3l2 9h10l2-6H5"/><circle cx="8" cy="13.5" r="1.3"/><circle cx="15" cy="13.5" r="1.3"/></svg>Zum Shop</div></article>
    <article class="card"><div class="card-title">Druckkleid, bunt</div><div class="card-media"><div class="dress" role="img" aria-label="Produktfoto: bunt bedrucktes Kleid"></div><span class="badge">- 24%</span></div><div class="card-price"><div class="price">37.99 €</div><div class="old">49.90 €</div><span class="ship">Versand: +5,95</span></div><div class="shop-btn"><svg width="20" height="16" viewBox="0 0 20 16" fill="none" stroke="#fff" stroke-width="1.5"><path d="M1 1h3l2 9h10l2-6H5"/><circle cx="8" cy="13.5" r="1.3"/><circle cx="15" cy="13.5" r="1.3"/></svg>Zum Shop</div></article>
    <article class="card"><div class="card-title">Druckkleid, bunt</div><div class="card-media"><div class="dress" role="img" aria-label="Produktfoto: bunt bedrucktes Kleid"></div></div></article>
    <article class="card"><div class="card-title">Druckkleid, bunt</div><div class="card-media"><div class="dress" role="img" aria-label="Produktfoto: bunt bedrucktes Kleid"></div></div></article>
    <article class="card"><div class="card-title">Druckkleid, bunt</div><div class="card-media"><div class="dress" role="img" aria-label="Produktfoto: bunt bedrucktes Kleid"></div></div></article>
    <article class="card"><div class="card-title">Druckkleid, bunt</div><div class="card-media"><div class="dress" role="img" aria-label="Produktfoto: bunt bedrucktes Kleid"></div></div></article>
  </main>
</div>
</body>
</html>
```